Webdesign für Realisation von  Bannern für unterschiedliche Werbenetzwerke
Webdesign für Realisation von Bannern für unterschiedliche Werbenetzwerke
Zielgruppe
Wir bieten Planung und Realistion von HTML5 Bannern für unterschiedliche Werbenetzwerke (besonders Velmora Adpilot) an.
Zielgruppe sind Unternehmen, welche einfach und kostengünstig online Banner erstellt haben möchten.
Aufgabenstellung
Die Webseite soll ein Onepager werden.
Die Webseite soll dem beigefügten Logo angepasst werden.
Bestellung und Bestätigung soll als eine Art Layover dargestellt werden.
Die Seite soll folgendes beinhalten:
- Header mit Logo, Telefon/Kontakt/Bestellbutton
- Intro
- Information zu Banner und Zielgruppenausrichtung -> Remarketing / ähnliche Zielgruppen / Keywords / Webseiteninhalt / gemeinsame Interessen / Lebensereignisse (Hochschulabschluss, Umzug, Ehe, (alles vorher/nachher). Diese Informationen gerne textlich wie grafisch darstellen
- Information zum Bestellvorgang. Diese Informationen gerne textlich wie grafisch darstellen.
- Kalkulation mit Bestellung (Bestellung führt dann zum erwähnten Layover)
- Portfolio (Vorschau von z.B. 3 Banner plus Aufklappfunktion für weitere Vorschläge)
- Footer
Beispielseite
https://www.flinkwerbung-studio.de/
An der Struktur dieser Webseite würden wir uns gerne anlehnen. Zielmarkt wird jedoch die Deutschschweiz sein.

```html
<!DOCTYPE html>
<html lang="de">
<head>
<meta charset="utf-8">
<title>Pixelfahne – HTML5-Banner</title>
<link rel="stylesheet" href="https://fonts.googleapis.com/css2?family=Roboto+Condensed:wght@300;400;700&display=swap">
<style>
:root{
  --blue:#1f6fc2;
  --blue-dark:#17579f;
  --blue-light:#2d7fd0;
  --orange:#f0561f;
  --orange-dark:#d9441a;
  --teal:#1aa79b;
  --green:#8cc63f;
  --yellow:#f4e11c;
  --red:#e84e1c;
  --grey-bg:#eef0f2;
  --grey-text:#8a8f96;
  --grey-soft:#9aa0a6;
  --grey-line:#c8ccd1;
  --white:#ffffff;
}
*{box-sizing:border-box;margin:0;padding:0}
html,body{width:1200px;height:2429px;overflow:hidden;background:var(--white)}
body{font-family:"Roboto Condensed",Arial,sans-serif;text-transform:uppercase;color:var(--grey-text)}
.page{position:relative;width:1200px;height:2429px;overflow:hidden}
.abs{position:absolute}

/* header */
.site-header{left:0;top:0;width:1200px;height:72px;background:var(--white);border-top:3px solid var(--blue)}
.brand{left:243px;top:10px;display:flex;align-items:center;gap:10px}
.brand-mark{width:46px;height:48px;background:var(--blue)}
.brand-name{font-weight:700;font-size:27px;color:var(--blue);letter-spacing:.5px;line-height:1}
.brand-tag{left:305px;top:48px;font-size:10px;letter-spacing:5px;color:var(--blue);font-weight:700}
.header-contact{left:700px;top:22px;width:256px}
.header-contact .kicker{font-size:8px;color:var(--grey-text)}
.header-contact .mail{display:flex;align-items:center;gap:6px;font-size:17px;color:var(--blue);font-weight:700;line-height:1.05}
.header-contact .call{font-size:10px;color:var(--grey-text);text-align:right}
.header-contact .call b{color:var(--blue);font-size:12px}

/* hero */
.hero{left:0;top:72px;width:1200px;height:279px;background:linear-gradient(120deg,var(--blue-light) 0%,var(--blue) 45%,var(--blue-dark) 100%);overflow:hidden}
.hero-device{left:312px;top:58px;width:240px;height:168px;border-radius:6px;background:linear-gradient(180deg,#dfe3e7,#8a929b)}
.hero-copy{right:289px;top:70px;text-align:right;color:var(--white)}
.hero-copy .lead{font-weight:300;font-size:18px;line-height:1.05}
.hero-copy .claim{font-weight:700;font-size:22px;line-height:1.05;margin-top:10px}
.btn{display:inline-block;background:linear-gradient(180deg,#f56a2d,var(--orange-dark));color:var(--white);font-weight:700;border-radius:2px;text-align:center;box-shadow:0 2px 3px rgba(0,0,0,.2)}
.hero-btn{right:289px;top:181px;width:173px;height:37px;line-height:37px;font-size:18px}
.more-tab{left:523px;top:333px;width:148px;height:31px;background:var(--blue-dark);color:var(--white);font-size:12px;font-weight:700;text-align:center;padding-top:4px;line-height:1.1}

/* steps */
.steps{left:0;top:364px;width:1200px;height:440px;background:var(--grey-bg)}
.steps-copy{right:312px;top:171px;text-align:right;width:560px}
.steps-copy .kicker{font-size:17px;color:var(--grey-text);font-weight:300;line-height:1}
.steps-copy h2{font-size:27px;line-height:.92;color:var(--blue);font-weight:700;margin-top:2px}
.steps-copy p{margin-top:18px;font-size:8.6px;line-height:1.32;font-weight:300;color:var(--grey-text)}
.steps-btn{right:312px;top:348px;width:164px;height:36px;line-height:36px;font-size:17px}

/* clients */
.clients{left:0;top:804px;width:1200px;height:268px;background:linear-gradient(180deg,var(--blue) 0%,var(--blue-dark) 100%);overflow:hidden}
.clients h2{left:0;top:22px;width:1200px;text-align:center;color:var(--white);font-size:25px;font-weight:700}
.client-banner{top:75px;width:187px;height:156px;border:1px solid rgba(255,255,255,.5)}
.client-banner .overlay-btn{position:absolute;left:28px;top:67px;width:130px;height:26px;line-height:26px;font-size:10px}
.nav-arrow{top:118px}

/* features */
.feature{width:312px;height:68px;background:var(--white);border-left:3px solid var(--blue);box-shadow:0 1px 3px rgba(0,0,0,.12);padding:8px 10px 0 52px}
.feature svg{position:absolute;left:14px;top:14px}
.feature h3{font-size:13px;color:var(--blue);font-weight:700}
.feature p{font-size:9px;line-height:1.25;color:var(--grey-text);font-weight:300}

/* pricing */
.pricing{left:0;top:1369px;width:1200px;height:628px;background:linear-gradient(100deg,#5b6f7f 0%,#c9cdd0 40%,#dedfdc 60%,#7d8c93 100%)}
.card{background:var(--white);border-top:4px solid var(--blue)}
.card-benefits{left:257px;top:1430px;width:304px;height:520px;border-bottom:6px solid var(--blue);padding:30px 15px 0 16px}
.card-benefits .kicker{font-size:17px;font-weight:300;color:var(--grey-text)}
.card-benefits h2{margin-top:20px;font-size:22px;line-height:1.05;font-weight:700;color:var(--blue)}
.benefit-list{list-style:none;margin-top:16px}
.benefit-list li{position:relative;padding-left:33px;font-size:13px;line-height:1.2;font-weight:300;margin-bottom:9px}
.benefit-list li svg{position:absolute;left:12px;top:2px}
.card-benefits .budget{margin-top:26px;font-size:17px;line-height:1.1;font-weight:700;color:var(--grey-soft)}
.card-benefits .note{margin-top:20px;font-size:17px;line-height:1.18;font-weight:300;color:var(--grey-text)}
.card-calc{left:591px;top:1430px;width:349px;height:515px}
.q{font-size:12px;color:var(--grey-text)}
.q b{color:var(--blue)}
.info{display:inline-block;width:8px;height:8px;border-radius:50%;background:var(--grey-soft);vertical-align:4px;margin-left:2px}
.type-visual{left:28px;top:62px;width:110px;height:80px;border-radius:40px;background:linear-gradient(90deg,#eceef0,#f4f5f6)}
.option{font-size:11px;display:flex;align-items:center;gap:10px}
.radio{width:18px;height:18px;border-radius:50%;background:#eceef0}
.qty{height:28px;line-height:28px;text-align:center;font-size:12px;color:var(--blue);background:#eef1f4}
.qty.active{background:var(--green);color:var(--white)}
.price-area{left:0;top:388px;width:349px;height:123px;background:#eceef0}
.price-label{font-size:22px;font-weight:300;color:var(--grey-soft)}
.price-value{font-size:25px;color:var(--grey-text)}
.price-sub{font-size:9px;color:var(--grey-soft)}
.offer-btn{left:117px;top:65px;width:219px;height:37px;line-height:37px;font-size:18px}
.footnote{left:6px;top:108px;width:338px;text-align:center;font-size:7px;line-height:1.1;color:var(--grey-soft)}

/* contact */
.contact{left:0;top:1997px;width:1200px;height:140px;text-align:center}
.contact .kicker{margin-top:36px;font-size:27px;font-weight:300;color:var(--grey-soft)}
.contact .line{font-size:27px;font-weight:700;color:var(--blue);margin-top:2px}
.contact .line span{font-weight:300;color:var(--grey-soft)}

/* to top + footer */
.to-top{left:0;top:2137px;width:1200px;height:29px;background:var(--teal);color:var(--white);font-size:12px;font-weight:700;display:flex;justify-content:center;align-items:center;gap:10px}
.site-footer{left:0;top:2166px;width:1200px;height:263px;background:linear-gradient(180deg,var(--blue) 0%,var(--blue-dark) 100%);color:var(--white);overflow:hidden}
.site-footer h4{font-size:13px;font-weight:700}
.site-footer p{font-size:12.5px;font-weight:300;line-height:1.45}
.footer-left{left:242px;top:32px;width:420px}
.footer-right{right:245px;top:32px;width:420px;text-align:right}
.address{margin-top:14px}
.address div{display:flex;align-items:center;gap:6px;font-size:12.5px;font-weight:300;line-height:1.5}
.legal{margin-top:16px;display:flex;gap:26px;font-size:13px;font-weight:700}
.badge{top:2361px;height:31px;background:var(--white)}
</style>
</head>
<body>
<div class="page">

  <header class="site-header abs">
    <div class="brand abs">
      <div class="brand-mark"></div>
      <div class="brand-name">PIXELFAHNE</div>
    </div>
    <div class="brand-tag abs">BANNER, DIE GEFALLEN.</div>
    <div class="header-contact abs">
      <div class="kicker">Schreiben Sie uns:</div>
      <div class="mail">
        <svg width="26" height="14" viewBox="0 0 26 14"><rect x="1" y="1" width="24" height="12" fill="none" stroke="#1f6fc2" stroke-width="1.4"/><path d="M1 1 L13 8 L25 1" fill="none" stroke="#1f6fc2" stroke-width="1.4"/></svg>
        INFO@PIXELFAHNE.CH
      </div>
      <div class="call">Oder rufen Sie uns an: <b>044 318 27 60</b></div>
    </div>
  </header>

  <section class="hero abs">
    <div class="hero-device abs" role="img" aria-label="Illustration eines aufgeklappten Laptops mit Banner-Motiv auf dem Bildschirm"></div>
    <div class="hero-copy abs">
      <div class="lead">Sie suchen den richtigen Partner<br>für Ihre nächste Online-Kampagne?</div>
      <div class="claim">Wir sind Ihre Experten für<br>professionelle HTML5-Banner!</div>
    </div>
    <a class="btn hero-btn abs">Jetzt kalkulieren</a>
  </section>
  <div class="more-tab abs">Mehr erfahren<br>
    <svg width="22" height="6" viewBox="0 0 22 6"><path d="M1 0 L6 5 L11 0 M11 0 L16 5 L21 0" fill="none" stroke="#fff" stroke-width="1"/></svg>
  </div>

  <section class="steps abs">
    <svg class="abs" style="left:0;top:0" width="1200" height="440" viewBox="0 364 1200 440">
      <path d="M290 600 H413 V565 H538 V530 H660 V493 H782 V460 H907 V764 H290 Z" fill="#fff" stroke="#c8ccd1" stroke-width="1"/>
      <g font-family="Roboto Condensed, Arial, sans-serif" text-anchor="middle" fill="#fff">
        <circle cx="351" cy="566" r="40" fill="#1f6fc2"/>
        <text x="351" y="572" font-size="30" font-weight="300">1</text><text x="351" y="586" font-size="8">BERATUNG</text>
        <circle cx="476" cy="531" r="40" fill="#8cc63f"/>
        <text x="476" y="537" font-size="30" font-weight="300">2</text><text x="476" y="551" font-size="8">VORSCHLAG</text>
        <circle cx="600" cy="497" r="40" fill="#f4e11c"/>
        <text x="600" y="503" font-size="30" font-weight="300">3</text><text x="600" y="517" font-size="8">FEEDBACK</text>
        <circle cx="721" cy="461" r="40" fill="#e84e1c"/>
        <text x="721" y="467" font-size="30" font-weight="300">4</text><text x="721" y="481" font-size="8">UMSETZUNG</text>
        <circle cx="845" cy="431" r="40" fill="#1aa79b"/>
        <text x="845" y="437" font-size="30" font-weight="300">5</text><text x="845" y="451" font-size="8">AUSLIEFERUNG</text>
      </g>
      <g fill="none" stroke="#8cc63f" stroke-width="4" stroke-linecap="round">
        <path d="M384 568 L392 576 L408 558"/>
        <path d="M509 533 L517 541 L533 523"/>
        <path d="M633 499 L641 507 L657 489"/>
        <path d="M754 463 L762 471 L778 453"/>
        <path d="M878 433 L886 441 L902 423"/>
      </g>
    </svg>
    <div class="steps-copy abs">
      <div class="kicker">Und so einfach geht´s</div>
      <h2>In fünf Schritten zum<br>fertigen HTML5-Banner</h2>
      <p>Im persönlichen Gespräch definieren wir gemeinsam Ihre Ziele. An welche Zielgruppe möchten Sie<br>welches Produkt vermarkten? Wie ist Ihr Zeitplan und wie Ihr Budget? Gemeinsam planen wir die<br>Bannerkampagne nach Ihren Wünschen. Nach unserem Gespräch erstellen wir Ihnen ein Angebot mit<br>verlässlichen Festpreisen. Jetzt geht es ins Detail! Wir entwickeln kreative Ideen, um Ihre Inhalte umzusetzen.<br>Dabei behalten wir immer Ihren Zeitplan und Ihr Budget im Auge. Wir finden die optimale Lösung<br>für Ihr Produkt. Mit aktuellster Technik programmieren wir Ihre Werbebanner sorgfältig und individuell.<br>Natürlich erfüllen unsere animierten HTML5-Banner alle Anforderungen Ihres Werbenetzwerkes.<br>Auf Wunsch übermitteln wir die Daten auch direkt an Ihren Medienpartner oder Publisher.</p>
    </div>
    <a class="btn steps-btn abs">Jetzt kalkulieren</a>
  </section>

  <section class="clients abs">
    <h2 class="abs">Kunden die unser Angebot nutzen:</h2>
    <svg class="nav-arrow abs" style="left:48px" width="24" height="40" viewBox="0 0 24 40"><path d="M22 2 L4 20 L22 38" fill="none" stroke="#fff" stroke-width="3.5"/></svg>
    <div class="client-banner abs" style="left:97px;background:linear-gradient(180deg,#2c4e7a,#1b2f4a)" role="img" aria-label="Kundenbanner: Tischtennisplatte mit Werbetext"></div>
    <div class="client-banner abs" style="left:303px;background:linear-gradient(90deg,#b9bcbf,#b8271f)" role="img" aria-label="Kundenbanner eines Immobilienmaklers mit Hausmotiv"></div>
    <div class="client-banner abs" style="left:507px;background:linear-gradient(180deg,#3a2a2a,#151010)" role="img" aria-label="Kundenbanner mit Produktflaschen">
      <a class="btn overlay-btn">Bannerset ansehen</a>
    </div>
    <div class="client-banner abs" style="left:712px;background:linear-gradient(180deg,#f2f2f2,#b3b5b7)" role="img" aria-label="Kundenbanner eines Automobilherstellers mit Fahrzeug und Preisangabe"></div>
    <div class="client-banner abs" style="left:918px;background:linear-gradient(180deg,#6b4b2f,#2c1d12)" role="img" aria-label="Kundenbanner für Kurs zum Holzhausbau"></div>
    <svg class="nav-arrow abs" style="left:1129px" width="24" height="40" viewBox="0 0 24 40"><path d="M2 2 L20 20 L2 38" fill="none" stroke="#fff" stroke-width="3.5"/></svg>
  </section>

  <div class="feature abs" style="left:270px;top:1136px">
    <svg width="28" height="40" viewBox="0 0 28 40"><path d="M4 4 L22 20 L4 36" fill="none" stroke="var(--green)" stroke-width="8" stroke-linejoin="round"/></svg>
    <h3>Kreative Banner</h3>
    <p>Lorem ipsum dolor sit amet, consetetur<br>sadipscing elitr, sed diam nonumy eirmod tempor<br>invidunt ut labore et dolore magna ...</p>
  </div>
  <div class="feature abs" style="left:616px;top:1136px">
    <svg width="28" height="40" viewBox="0 0 28 40"><path d="M4 4 L22 20 L4 36" fill="none" stroke="var(--yellow)" stroke-width="8" stroke-linejoin="round"/></svg>
    <h3>Unterschiedliche Werbenetzwerke</h3>
    <p>Lorem ipsum dolor sit amet, consetetur<br>sadipscing elitr, sed diam nonumy eirmod tempor<br>invidunt ut labore et dolore magna ...</p>
  </div>
  <div class="feature abs" style="left:270px;top:1235px">
    <svg width="28" height="40" viewBox="0 0 28 40"><path d="M4 4 L22 20 L4 36" fill="none" stroke="var(--red)" stroke-width="8" stroke-linejoin="round"/></svg>
    <h3>Rasche Umsetzung</h3>
    <p>Lorem ipsum dolor sit amet, consetetur<br>sadipscing elitr, sed diam nonumy eirmod tempor<br>invidunt ut labore et dolore magna ...</p>
  </div>
  <div class="feature abs" style="left:616px;top:1235px">
    <svg width="28" height="40" viewBox="0 0 28 40"><path d="M4 4 L22 20 L4 36" fill="none" stroke="var(--teal)" stroke-width="8" stroke-linejoin="round"/></svg>
    <h3>Attraktive Preise</h3>
    <p>Lorem ipsum dolor sit amet, consetetur<br>sadipscing elitr, sed diam nonumy eirmod tempor<br>invidunt ut labore et dolore magna ...</p>
  </div>

  <section class="pricing abs" role="img" aria-label="Unscharfes Foto eines Teams im Büro bei der Besprechung"></section>

  <div class="card card-benefits abs">
    <div class="kicker">HTML5-Banner zu Festpreisen</div>
    <h2>Ihre Vorteile<br>auf einen Blick</h2>
    <ul class="benefit-list">
      <li><svg width="14" height="10" viewBox="0 0 14 10"><path d="M1 5 L5 9 L13 1" fill="none" stroke="#1f6fc2" stroke-width="1.6"/></svg>Persönliche Beratung</li>
      <li><svg width="14" height="10" viewBox="0 0 14 10"><path d="M1 5 L5 9 L13 1" fill="none" stroke="#1f6fc2" stroke-width="1.6"/></svg>Entwicklung nach Vorgaben</li>
      <li><svg width="14" height="10" viewBox="0 0 14 10"><path d="M1 5 L5 9 L13 1" fill="none" stroke="#1f6fc2" stroke-width="1.6"/></svg>Ihrer Werbenetzwerke<br>auf Wunsch direkte Lieferung<br>an Ihre Mediaagentur oder<br>Publisher wie Velmora Display,<br>Tandemklick, Rollwerk, Formatix usw.</li>
    </ul>
    <div class="budget">Mit unseren Festpreisen<br>bleiben Sie immer im Budget.</div>
    <div class="note">Die folgenden Preise sind für<br>Standardformate.<br>Natürlich machen wir Ihnen<br>auch gerne ein persönliches<br>Angebot für Sonderformate,<br>Interaktion und Rich Media.</div>
  </div>

  <div class="card card-calc abs">
    <div class="q abs" style="left:12px;top:34px"><b>1.</b> Welche Art Banner benötigen Sie? <span class="info"></span></div>
    <div class="type-visual abs" role="img" aria-label="Auswahlsymbol für HTML5-Banner, ausgewählt"></div>
    <div class="q abs" style="left:12px;top:182px"><b>2.</b> Gibt es eine Designvorlage? <span class="info"></span></div>
    <div class="option abs" style="left:28px;top:206px">
      <svg width="22" height="18" viewBox="0 0 22 18"><path d="M2 9 L8 15 L20 2" fill="none" stroke="#8cc63f" stroke-width="3.5"/></svg>Designvorlagen vorhanden
    </div>
    <div class="option abs" style="left:28px;top:236px"><span class="radio"></span><span><b style="color:#8a8f96">Keine</b> Designvorlage vorhanden</span></div>
    <div class="q abs" style="left:12px;top:276px"><b>3.</b> Wieviele Banner benötigen Sie? <span class="info"></span></div>
    <div class="qty abs" style="left:29px;top:311px;width:38px">01</div>
    <div class="qty abs" style="left:71px;top:311px;width:38px">02</div>
    <div class="qty active abs" style="left:113px;top:311px;width:38px">03</div>
    <div class="qty abs" style="left:156px;top:311px;width:38px">04</div>
    <div class="qty abs" style="left:198px;top:311px;width:38px">05</div>
    <div class="qty abs" style="left:240px;top:311px;width:38px">06</div>
    <div class="qty abs" style="left:283px;top:311px;width:38px">08</div>
    <div class="qty abs" style="left:29px;top:348px;width:38px">10</div>
    <div class="qty abs" style="left:71px;top:348px;width:38px">12</div>
    <div class="qty abs" style="left:113px;top:348px;width:38px">16</div>
    <div class="qty abs" style="left:156px;top:348px;width:165px">Andere Anzahl Banner</div>
    <div class="price-area abs">
      <div class="price-label abs" style="left:10px;top:10px">Kampagnenpreis*:</div>
      <div class="price-sub abs" style="left:11px;top:40px">zzgl. 7,7% MwSt.</div>
      <div class="price-value abs" style="right:12px;top:8px">1000,00 €</div>
      <div class="price-sub abs" style="right:12px;top:40px;font-size:10px">77,00 €</div>
      <a class="btn offer-btn abs">Angebot anfragen</a>
      <div class="footnote abs">* Es handelt sich hier um erste Richtpreise. Fragen Sie einfach unverbindlich<br>an, dann machen wir Ihnen ein konkretes Angebot!</div>
    </div>
  </div>

  <section class="contact abs">
    <div class="kicker">Wir beraten Sie gerne:</div>
    <div class="line">044 318 27 60 <span>oder</span> per E-Mail</div>
  </section>

  <div class="to-top abs">
    <svg width="12" height="8" viewBox="0 0 12 8"><path d="M1 7 L6 2 L11 7" fill="none" stroke="#fff" stroke-width="1.5"/></svg>
    Nach oben
    <svg width="12" height="8" viewBox="0 0 12 8"><path d="M1 7 L6 2 L11 7" fill="none" stroke="#fff" stroke-width="1.5"/></svg>
  </div>

  <footer class="site-footer abs">
    <div class="footer-left abs">
      <h4>Kontaktieren Sie uns</h4>
      <p style="margin-top:20px">Gerne sind wir auch persönlich für Sie ansprechbar.<br>Wir freuen uns auf Ihre Anfrage.</p>
      <div class="address">
        <div><svg width="14" height="16" viewBox="0 0 14 16"><path d="M7 15 C3 10 2 8 2 6 A5 5 0 0 1 12 6 C12 8 11 10 7 15 Z" fill="#fff"/><circle cx="7" cy="6" r="2" fill="#1f6fc2"/></svg>Kreisfeld Medien GmbH</div>
        <div style="padding-left:20px">Talgasse 8, 8004 Zürich</div>
        <div><svg width="14" height="14" viewBox="0 0 14 14"><path d="M10 1 C6 3 3 7 3 13" fill="none" stroke="#fff" stroke-width="2"/></svg>044 318 27 60</div>
        <div><svg width="14" height="10" viewBox="0 0 14 10"><rect x=".5" y=".5" width="13" height="9" fill="none" stroke="#fff"/><path d="M.5 .5 L7 6 L13.5 .5" fill="none" stroke="#fff"/></svg>post@kreisfeld-medien.ch</div>
      </div>
      <div class="legal"><span>Impressum</span><span>Datenschutz</span></div>
    </div>
    <div class="footer-right abs">
      <h4>Mehr über uns</h4>
      <p style="margin-top:20px">HTML5-Banner-Werbung ist eine Dienstleistung<br>der Zürcher Full-Service-Medienagentur Firma.</p>
      <p style="margin-top:18px">Auf kreisfeld-medien.ch erfahren Sie, in welchen<br>Bereichen wir Sie noch unterstützen können.</p>
    </div>
  </footer>
  <div class="badge abs" style="left:808px;width:89px"></div>
  <div class="badge abs" style="left:912px;width:43px"></div>

</div>
</body>
</html>
```